Contemporary Elegant Business Card Design for an International Trade Company in the Wine Industry

We need a new business card design for an international trade company in the wine and winemaking industry. The overall feel of the card should be contemporary, upscale, luxurious and elegant. It should communicate confidence and professionalism. The colors should complementary to our logo design (burgundy, gold, and black).
Inspiration: rich velvet tapestry
The card should include the following information:
Business: Brovenna Trading/Shipping, LLC.
Name: Marcus T. Hollenbrand
Title: CEO
Email: mark@brovennatrading.example
Phone: 555-294-6172
www.brovennatrading.example
Updates
Project Deadline Extended
Reason: We'd like the designers that we requested some additional designs from to still submit designs. Thank you!
Industry/Entity Type
Business
Contact Information for Business Card
Title: CEO
Phone: 555-294-6172
www.brovennatrading.example
Look and feel

```html
<!DOCTYPE html>
<html lang="en">
<head>
<meta charset="utf-8">
<title>Brovenna Trading/Shipping — Business Card</title>
<link rel="stylesheet" href="https://fonts.googleapis.com/css2?family=Russo+One&family=PT+Sans:wght@400;700&family=Alegreya+Sans+SC:wght@500;700&display=swap">
<style>
  :root {
    --backdrop: #e9e6e2;
    --burgundy: #a30f17;
    --burgundy-deep: #4e0508;
    --rose: #b33552;
    --gold-light: #f6dc92;
    --gold: #e8c26a;
    --ink: #2b2214;
    --crimson: #9b1b45;
    --white: #ffffff;
  }
  * { box-sizing: border-box; margin: 0; padding: 0; }
  html, body { width: 1200px; height: 800px; overflow: hidden; }
  body {
    background: var(--backdrop);
    display: flex;
    align-items: center;
    justify-content: center;
    gap: 60px;
  }
  .card {
    position: relative;
    width: 500px;
    height: 286px;
    overflow: hidden;
    box-shadow: 0 8px 22px rgba(0,0,0,0.25);
  }

  /* Back side: contact details on gold */
  .card--back {
    background: linear-gradient(135deg, var(--gold-light), var(--gold));
    color: var(--ink);
  }
  .card--back .map-texture {
    position: absolute;
    inset: 70px 30px 20px 120px;
    background: radial-gradient(ellipse at center, rgba(200,160,80,0.28), rgba(200,160,80,0) 70%);
  }
  .card--back .brand {
    position: absolute;
    top: 32px;
    left: 32px;
    display: flex;
    align-items: center;
    gap: 12px;
  }
  .brand__square {
    width: 46px;
    height: 46px;
    background: var(--rose);
  }
  .brand__name {
    font-family: "Russo One", sans-serif;
    font-size: 26px;
    letter-spacing: 1px;
    color: var(--ink);
  }
  .contact {
    position: absolute;
    right: 36px;
    bottom: 34px;
    text-align: right;
    font-family: "PT Sans", sans-serif;
    font-size: 15px;
    line-height: 1.55;
  }
  .contact__name {
    font-family: "Alegreya Sans SC", sans-serif;
    font-weight: 700;
    font-size: 24px;
    color: var(--crimson);
    letter-spacing: 1px;
  }
  .contact__title { margin-bottom: 12px; }

  /* Front side: burgundy with logotype */
  .card--front {
    background: linear-gradient(120deg, var(--burgundy) 0%, #7d0a10 60%, var(--burgundy-deep) 100%);
    color: var(--white);
  }
  .card--front .map-texture {
    position: absolute;
    inset: 40px 30px 40px 150px;
    background: radial-gradient(ellipse at center, rgba(60,0,4,0.35), rgba(60,0,4,0) 70%);
  }
  .card--front .brand {
    position: absolute;
    top: 50%;
    left: 40px;
    transform: translateY(-50%);
    display: flex;
    align-items: center;
    gap: 22px;
  }
  .card--front .brand__square {
    width: 92px;
    height: 92px;
  }
  .card--front .brand__name {
    font-size: 50px;
    color: var(--white);
    line-height: 1;
  }
  .brand__tagline {
    margin-top: 8px;
    font-family: "Russo One", sans-serif;
    font-size: 17px;
    color: var(--white);
    letter-spacing: 0.5px;
  }
</style>
</head>
<body>
  <section class="card card--back" aria-label="Business card back">
    <div class="map-texture" role="img" aria-label="Faint world map texture"></div>
    <div class="brand">
      <span class="brand__square"></span>
      <span class="brand__name">BROVENNA</span>
    </div>
    <div class="contact">
      <p class="contact__name">Marcus T. Hollenbrand</p>
      <p class="contact__title">CEO</p>
      <p>555-294-6172</p>
      <p>mark@brovennatrading.example</p>
      <p>www.brovennatrading.example</p>
    </div>
  </section>

  <section class="card card--front" aria-label="Business card front">
    <div class="map-texture" role="img" aria-label="Subtle world map texture"></div>
    <div class="brand">
      <span class="brand__square"></span>
      <div>
        <p class="brand__name">BROVENNA</p>
        <p class="brand__tagline">Trading and Shipping</p>
      </div>
    </div>
  </section>
</body>
</html>
```